Professional and modern website for Real Estate services company

Hi there! We're looking for a responsive, highly professional and modern (in line with Latest trends) coded website for a Real Estate services company named Portalia (find logo attached). I will try to Explain how I picture it in my head, but feel free to step out of the script and design it as you please. The structure for the website must be as Follows: - Menu: at the top of the screen, always visible (in any page and when to scrolling down). Logo at the left hand side (clicking redirects to home), then a Services, About us, Blog and Contact and on the right hand, Estimate and Log in (just placeholder, no log in required yet). - Home: (I like https://fr.domvera.example/): a landscape picture of Madrid's skyline. Very important That at a first glance (without scrolling) you can see a box to input data of your building to get an estimate (Post code, Number of homes, Number of garages, Number of stores, Swimming pool (yes / no) Concierge (yes / no)). Should there be a small space Also for a corporate presentation video (more or less like https://www.velbrastahogares.example/ but With the estimate Request box INSTEAD OF the App - however, do not take this one as example Given I just wanted to illustrate the structure). Still in the Home, bellow the first glance, I'd like to have a brief introduction of the following pages (Services, About us, Blog and Contact). This can be in a Either "square" form (like https://fr.domvera.example/) or in a "scroll" form (like https://k7pisos.example/). - Services: we offer 3 sets of services, each of them composed by three specific services, Namely: * Administration Treasury Accounting Savings * Consulting Legal Technical Regulatory * Mediation Repairs Meetings Delinquency For the sake of structuring, each of the nine services will Have to written description composed of 3 small paragraphs of About 15 words. I Tend to like to Accompany With each of the services related icons / vectors, but feel free to design them as you want. - About us: content not yet defined, but will be a series of bullets / sections in Which We talk about prep or differentiating points. We can include the corporate video presentation here again. - Blog: just a space Where you can see to the blog entries (in Home, probably just show 3/4). - Contact: a fancy contact form, with map, address, telephone, e-mail and opening hours. Just to give it a bit more content, maybe include a catch phrase like "We're looking forward to meeting you!" or something like that. - Estimate: this is the Most Important page in the website (in Addition to the upper part of the Home page). Basically replicate the estimate for the home box, but maybe with a bit more design or extended, Given this is a single page just for that. - Log in: opens a drop-down with user and password (just placeholder, no log in required yet). Regarding colors, we still do not Have a color scheme, so anything in line With the logo is OK. Many thanks in advance, Martin

All ages and genders

Real Estate

Coded - Design and coding required

5+ page

Sans Serif

Must have
• Blank colored background

```html
<!DOCTYPE html>
<html lang="en">
<head>
<meta charset="utf-8">
<title>Portalia — Real Estate Services</title>
<link rel="stylesheet" href="https://fonts.googleapis.com/css2?family=Lato:wght@400;700;900&family=Courgette&display=swap">
<style>
:root{
  --orange:#d36a0b;
  --orange-dark:#b85a06;
  --teal:#17b4b6;
  --teal-dark:#0f9ea1;
  --ink:#3b3b3b;
  --paper:#eceae7;
  --navy:#1f2b37;
  --navy-deep:#141d27;
  --white:#ffffff;
  --field-border:#8a8a8a;
  --brand-grey:#4a4a4a;
}
*{box-sizing:border-box;margin:0;padding:0}
html,body{width:1200px;height:2293px;overflow:hidden}
body{position:relative;background:var(--paper);font-family:"Lato",Arial,sans-serif;color:var(--ink)}

/* header */
.site-header{position:absolute;left:0;top:0;width:1200px;height:104px;background:var(--paper)}
.brand{position:absolute;left:70px;top:30px;font-size:40px;font-weight:700;color:var(--brand-grey);line-height:1}
.main-nav a{position:absolute;top:64px;font-size:16px;font-weight:700;color:#333;text-decoration:none;letter-spacing:.5px}
.btn-head{position:absolute;top:54px;height:37px;border-radius:5px;background:var(--orange);color:var(--white);font-size:16px;font-weight:700;display:flex;align-items:center;justify-content:center;letter-spacing:.5px}

/* hero */
.hero{position:absolute;left:0;top:104px;width:1200px;height:442px;background:linear-gradient(180deg,#7d95b0 0%,#a8b8c8 45%,#8b8f98 70%,#5a4a46 100%)}
.hero-title{position:absolute;left:0;width:1200px;top:165px;text-align:center;font-family:"Courgette",cursive;font-weight:400;font-size:39px;color:var(--white);text-shadow:0 2px 4px rgba(0,0,0,.35)}
.hero-sub{position:absolute;left:0;width:1200px;top:218px;text-align:center;font-size:17px;font-weight:700;color:var(--white);letter-spacing:.6px;text-shadow:0 1px 3px rgba(0,0,0,.4)}

/* estimate */
.estimate{position:absolute;left:78px;top:584px;width:544px;height:333px;border:12px solid #555;background:#e8e6e3}
.estimate-head{height:49px;background:var(--orange);color:var(--white);font-size:23px;font-weight:700;padding:12px 18px 0}
.field-label{position:absolute;font-size:15px;font-weight:700;color:#666}
.field{position:absolute;width:210px;height:30px;background:#f6f6f6;border:1.5px solid var(--field-border);border-radius:3px}
.choice{position:absolute;font-size:14px;color:#666;display:flex;gap:8px;align-items:center}
.box{display:inline-block;width:13px;height:13px;border:1.5px solid #777;background:#fff;margin-right:12px}
.btn-submit{position:absolute;left:29px;top:265px;width:174px;height:30px;background:var(--orange);color:var(--white);font-size:12px;font-weight:900;border-radius:3px;display:flex;align-items:center;justify-content:center;letter-spacing:.6px}

/* video */
.video{position:absolute;left:640px;top:584px;width:479px;height:333px;background:#0d0d0d}
.video-frame{position:absolute;left:0;top:26px;width:479px;height:280px;background:linear-gradient(180deg,#6f8bb0 0%,#b9c4cf 40%,#8c8272 62%,#5e5446 100%)}
.video-tool{position:absolute;right:8px;width:32px;height:34px;background:rgba(20,20,20,.85);border-radius:3px}
.video-bar{position:absolute;left:14px;right:8px;bottom:10px;height:30px;background:rgba(15,15,15,.85);border-radius:2px}
.video-time{position:absolute;left:165px;top:277px;background:#222;color:#fff;font-size:11px;padding:2px 6px}

/* services */
.services{position:absolute;left:0;top:966px;width:1200px;height:462px;background:linear-gradient(180deg,#4d6079 0%,#6e7f93 55%,#8b8d8f 100%)}
.services-title{position:absolute;left:0;width:1200px;top:34px;text-align:center;font-size:42px;font-weight:700;color:var(--white);letter-spacing:1.5px}
.service-card{position:absolute;top:106px;width:325px;height:301px}
.service-head{height:104px;background:rgba(255,255,255,.22);display:flex;align-items:center;padding-left:30px;gap:18px;color:var(--white);font-size:23px;letter-spacing:1px}
.service-item{height:65.7px;background:rgba(211,106,11,.82);border-bottom:1px solid rgba(140,60,0,.35);display:flex;align-items:center;padding-left:30px;gap:14px;color:var(--white)}
.service-item b{display:block;font-size:15px}
.service-item span{display:block;font-size:11px;font-weight:700}

/* intro cards */
.intro-card{position:absolute;top:1472px;width:324px;height:324px}
.intro-head{height:57px;display:flex;align-items:center;justify-content:center;color:var(--white);font-size:20px;font-weight:700;letter-spacing:1px}
.card-about,.card-contact{background:var(--teal)}
.card-about .intro-head,.card-contact .intro-head{background:var(--teal-dark)}
.card-blog{background:var(--orange)}
.card-blog .intro-head{background:var(--orange-dark)}
.bullet{position:absolute;left:20px;font-size:13.5px;font-weight:700;color:var(--white);display:flex;align-items:center;gap:10px}
.bullet i{width:11px;height:11px;border-radius:50%;background:var(--orange);display:inline-block}
.mini-video{position:absolute;left:35px;top:159px;width:245px;height:141px;background:linear-gradient(180deg,#7a8796 0%,#4b5560 55%,#2b3037 100%)}
.post{position:absolute;left:14px;display:flex;gap:8px}
.post-date{width:64px;height:52px;background:var(--white);border:2px solid #8a4a10;color:#555;font-size:18px;font-weight:700;text-align:center;line-height:23px}
.post-title{color:var(--white);font-size:16px;font-weight:900;letter-spacing:.5px;margin-top:4px}
.post-text{color:#fde1c4;font-size:12.5px;margin-top:3px}
.c-field{position:absolute;height:24px;background:var(--white);border:1px solid #888;font-size:11px;color:#777;padding:4px 6px}
.c-submit{position:absolute;left:23px;top:150px;width:276px;height:23px;background:#555;border-radius:3px;color:var(--white);font-size:11px;font-weight:900;display:flex;align-items:center;justify-content:center;letter-spacing:.6px}
.map{position:absolute;left:23px;top:182px;width:276px;height:104px;background:linear-gradient(135deg,#e8e3d6 0%,#d9d8cf 50%,#c9d6c4 100%)}
.quote{position:absolute;left:0;width:324px;top:298px;text-align:center;font-size:13.5px;font-weight:700;color:var(--white)}

/* band */
.band{position:absolute;left:0;top:1842px;width:1200px;height:103px;background:var(--orange)}
.band .brand{left:102px;top:30px;font-size:42px}
.band-tag{position:absolute;left:468px;top:37px;font-size:23px;font-weight:700;color:var(--white);letter-spacing:.3px}
.social{position:absolute;top:34px;width:45px;height:45px;border-radius:2px}

/* footer */
.site-footer{position:absolute;left:0;top:1945px;width:1200px;height:289px;background:var(--navy)}
.foot-col{position:absolute;top:42px}
.foot-col h4{font-size:17px;color:var(--orange);font-weight:700;letter-spacing:.3px;margin-bottom:18px}
.foot-col p{font-size:14.5px;color:var(--white);line-height:23px}
.foot-col li{list-style:none;font-size:14.5px;color:var(--white);line-height:29px}
.news-field{width:217px;height:35px;background:var(--white);display:flex;align-items:center;gap:10px;padding-left:10px;font-size:14px;color:#888}
.news-btn{width:217px;height:33px;background:var(--orange);color:var(--white);font-size:13px;font-weight:700;display:flex;align-items:center;justify-content:center;margin-top:11px;letter-spacing:.4px}
.copyright{position:absolute;left:0;top:2234px;width:1200px;height:59px;background:var(--navy-deep);color:var(--white);font-size:15px;display:flex;align-items:center;justify-content:center;letter-spacing:.4px}
</style>
</head>
<body>

<header class="site-header">
  <div class="brand">Portalia</div>
  <nav class="main-nav">
    <a style="left:436px">HOME</a>
    <a style="left:512px">SERVICES</a>
    <a style="left:619px">ABOUT US</a>
    <a style="left:729px">BLOG</a>
    <a style="left:798px">CONTACT</a>
  </nav>
  <div class="btn-head" style="left:902px;width:104px">ESTIMATE</div>
  <div class="btn-head" style="left:1015px;width:103px">LOGIN</div>
</header>

<section class="hero">
  <div role="img" aria-label="Madrid city skyline under a cloudy sky" style="position:absolute;inset:0"></div>
  <h1 class="hero-title">Find your perfect New Home and start a new life</h1>
  <p class="hero-sub">Lorem Ipsum has been the industry's standard dummy text ever since the 1500s,</p>
</section>

<form class="estimate">
  <div class="estimate-head">Estimate Property</div>
  <span class="field-label" style="left:29px;top:76px">Post Code</span>
  <span class="field-label" style="left:279px;top:76px">Number of Stores</span>
  <span class="field" style="left:29px;top:99px"></span>
  <span class="field" style="left:279px;top:99px"></span>
  <span class="field-label" style="left:29px;top:143px">Number of Homes</span>
  <span class="field-label" style="left:279px;top:143px">Number of garages</span>
  <span class="field" style="left:29px;top:164px"></span>
  <span class="field" style="left:279px;top:164px"></span>
  <span class="field-label" style="left:29px;top:214px">Swimming Pool</span>
  <span class="field-label" style="left:279px;top:214px">Concierge</span>
  <span class="choice" style="left:29px;top:240px">Yes <span class="box"></span> No <span class="box"></span></span>
  <span class="choice" style="left:279px;top:240px">Yes <span class="box"></span> No <span class="box"></span></span>
  <div class="btn-submit">SUBMIT</div>
</form>

<div class="video">
  <div class="video-frame" role="img" aria-label="Corporate presentation video: dirt road through a dry field under mountains"></div>
  <div class="video-tool" style="top:22px"><svg width="32" height="34"><path d="M16 22 L9 15 a4 4 0 0 1 7-5 a4 4 0 0 1 7 5 Z" fill="#fff"/></svg></div>
  <div class="video-tool" style="top:60px"><svg width="32" height="34"><circle cx="11" cy="17" r="3" fill="#fff"/><circle cx="21" cy="11" r="3" fill="#fff"/><circle cx="21" cy="23" r="3" fill="#fff"/><path d="M11 17 L21 11 M11 17 L21 23" stroke="#fff" stroke-width="1.5"/></svg></div>
  <div class="video-tool" style="top:98px"><svg width="32" height="34"><path d="M12 12 L7 17 L12 22 M20 12 L25 17 L20 22 M18 10 L14 24" stroke="#fff" stroke-width="2" fill="none"/></svg></div>
  <div class="video-tool" style="top:136px"><svg width="32" height="34"><text x="16" y="21" text-anchor="middle" font-family="Lato,sans-serif" font-weight="900" font-size="12" fill="#2aa8e0">HD</text></svg></div>
  <div class="video-bar">
    <svg width="457" height="30">
      <rect x="10" y="8" width="4" height="14" fill="#fff"/><rect x="17" y="8" width="4" height="14" fill="#fff"/>
      <rect x="48" y="13" width="330" height="5" fill="#555"/><rect x="48" y="13" width="96" height="5" fill="#2aa8e0"/>
      <rect x="388" y="9" width="24" height="12" fill="none" stroke="#2aa8e0" stroke-width="1.5"/>
      <path d="M428 9 h6 M428 9 v6 M447 21 h-6 M447 21 v-6" stroke="#fff" stroke-width="2"/>
    </svg>
  </div>
  <div class="video-time">00:40</div>
</div>

<section class="services">
  <div role="img" aria-label="Faded photo of Madrid office towers" style="position:absolute;inset:0"></div>
  <h2 class="services-title">OUR SERVICES</h2>

  <div class="service-card" style="left:92px">
    <div class="service-head"><svg width="48" height="48" fill="none" stroke="#fff" stroke-width="3"><circle cx="18" cy="14" r="9"/><path d="M4 44 v-6 a14 14 0 0 1 24 -8"/><circle cx="36" cy="36" r="6"/></svg>ADMINISTRATION</div>
    <div class="service-item"><svg width="40" height="36" fill="#fff"><path d="M20 2 L38 11 H2 Z"/><rect x="6" y="13" width="4" height="15"/><rect x="14" y="13" width="4" height="15"/><rect x="22" y="13" width="4" height="15"/><rect x="30" y="13" width="4" height="15"/><rect x="2" y="30" width="36" height="4"/></svg><div><b>Treasury</b><span>Lorem Ipsum has been the dummy.</span></div></div>
    <div class="service-item"><svg width="40" height="36" fill="#fff"><ellipse cx="20" cy="8" rx="14" ry="5"/><ellipse cx="20" cy="18" rx="14" ry="5"/><ellipse cx="20" cy="28" rx="14" ry="5"/></svg><div><b>Savings</b><span>Lorem Ipsum has been the dummy.</span></div></div>
    <div class="service-item"><svg width="40" height="36" fill="none" stroke="#fff" stroke-width="3"><rect x="9" y="2" width="22" height="32" rx="3"/><rect x="13" y="7" width="14" height="6"/><path d="M14 19h2M20 19h2M14 25h2M20 25h2M14 30h2M20 30h2"/></svg><div><b>Accounting</b><span>Lorem Ipsum has been the dummy.</span></div></div>
  </div>

  <div class="service-card" style="left:436px">
    <div class="service-head"><svg width="60" height="40" fill="none" stroke="#fff" stroke-width="3"><path d="M2 12 L16 6 L30 14 L44 6 L58 12 M12 22 L26 34 L34 30 L44 22 M30 14 L22 22"/></svg>CONSULTING</div>
    <div class="service-item"><svg width="40" height="36" fill="none" stroke="#fff" stroke-width="2.5"><path d="M20 3 V32 M8 8 H32 M12 32 H28 M8 8 L3 20 H13 Z M32 8 L27 20 H37 Z"/></svg><div><b>Legal</b><span>Lorem Ipsum has been the dummy.</span></div></div>
    <div class="service-item"><svg width="40" height="36" fill="none" stroke="#fff" stroke-width="2.5"><circle cx="20" cy="12" r="8"/><circle cx="20" cy="12" r="3" fill="#fff"/><path d="M6 34 a14 12 0 0 1 28 0 Z" fill="#fff"/></svg><div><b>Technical</b><span>Lorem Ipsum has been the dummy.</span></div></div>
    <div class="service-item"><svg width="40" height="36" fill="none" stroke="#fff" stroke-width="2.5"><rect x="8" y="4" width="20" height="28" rx="2"/><path d="M12 11h12M12 17h12M12 23h7"/><circle cx="29" cy="28" r="6" fill="#fff"/><path d="M26 28 l2 2 l4 -4" stroke="#c0620a" stroke-width="2"/></svg><div><b>Regulatory</b><span>Lorem Ipsum has been the dummy.</span></div></div>
  </div>

  <div class="service-card" style="left:781px">
    <div class="service-head"><svg width="60" height="44" fill="#fff"><circle cx="30" cy="11" r="8"/><path d="M16 38 a14 13 0 0 1 28 0 Z"/><circle cx="11" cy="17" r="6"/><path d="M0 40 a11 10 0 0 1 18 -7 v7 Z"/><circle cx="49" cy="17" r="6"/><path d="M60 40 a11 10 0 0 0 -18 -7 v7 Z"/></svg>MEDIATION</div>
    <div class="service-item"><svg width="40" height="36" fill="none" stroke="#fff" stroke-width="3.5"><path d="M6 4 L34 32 M34 4 L6 32"/></svg><div><b>Repairs</b><span>Lorem Ipsum has been the dummy.</span></div></div>
    <div class="service-item"><svg width="40" height="36" fill="#fff"><rect x="8" y="16" width="24" height="4"/><circle cx="12" cy="8" r="4"/><circle cx="28" cy="8" r="4"/><rect x="5" y="22" width="4" height="12"/><rect x="31" y="22" width="4" height="12"/><rect x="18" y="20" width="4" height="14"/></svg><div><b>Meetings</b><span>Lorem Ipsum has been the dummy.</span></div></div>
    <div class="service-item"><svg width="40" height="36" fill="none" stroke="#fff" stroke-width="2.5"><path d="M4 6 h20 v14 h-12 l-6 5 v-5 h-2 Z"/><path d="M28 12 h8 v14 h-2 v5 l-6 -5 h-10 v-4"/></svg><div><b>Delinquency</b><span>Lorem Ipsum has been the dummy.</span></div></div>
  </div>
</section>

<section class="intro-card card-about" style="left:95px">
  <div class="intro-head">ABOUT US</div>
  <div class="bullet" style="top:70px"><i></i>Lorem Ipsum has been the dummy...</div>
  <div class="bullet" style="top:98px"><i></i>Lorem Ipsum has been the dummy...</div>
  <div class="bullet" style="top:125px"><i></i>Lorem Ipsum has been the dummy...</div>
  <div class="mini-video" role="img" aria-label="Corporate video still: waves at a rocky shore at dusk">
    <svg width="245" height="141" style="position:absolute;left:0;top:0">
      <rect x="221" y="4" width="20" height="16" fill="#222"/><rect x="221" y="22" width="20" height="16" fill="#222"/><rect x="221" y="40" width="20" height="16" fill="#222"/>
      <rect x="0" y="123" width="245" height="18" fill="rgba(0,0,0,.75)"/>
      <path d="M12 127 L19 132 L12 137 Z" fill="#fff"/>
      <rect x="40" y="130" width="100" height="3" fill="#666"/><rect x="40" y="130" width="22" height="3" fill="#2aa8e0"/>
    </svg>
  </div>
</section>

<section class="intro-card card-blog" style="left:439px">
  <div class="intro-head">BLOG</div>
  <div class="post" style="top:72px"><div class="post-date">03<br>DEC</div><div><div class="post-title">LOREM IPSUM</div><div class="post-text">Lorem Ipsum has been the dummy.</div></div></div>
  <div class="post" style="top:130px"><div class="post-date">03<br>DEC</div><div><div class="post-title">LOREM IPSUM</div><div class="post-text">Lorem Ipsum has been the dummy.</div></div></div>
  <div class="post" style="top:188px"><div class="post-date">03<br>DEC</div><div><div class="post-title">LOREM IPSUM</div><div class="post-text">Lorem Ipsum has been the dummy.</div></div></div>
  <div class="post" style="top:246px"><div class="post-date">03<br>DEC</div><div><div class="post-title">LOREM IPSUM</div><div class="post-text">Lorem Ipsum has been the dummy.</div></div></div>
</section>

<section class="intro-card card-contact" style="left:783px">
  <div class="intro-head">CONTACT US</div>
  <div class="c-field" style="left:23px;top:68px;width:86px">Email</div>
  <div class="c-field" style="left:117px;top:68px;width:86px">Open Hours</div>
  <div class="c-field" style="left:212px;top:68px;width:87px">Phone</div>
  <div class="c-field" style="left:23px;top:104px;width:276px;height:38px">Adress</div>
  <div class="c-submit">SUBMIT</div>
  <div class="map" role="img" aria-label="Street map of the office area with location pins"></div>
  <p class="quote">"We're looking forward to meeting you!"</p>
</section>

<section class="band">
  <div class="brand">Portalia</div>
  <p class="band-tag">Best Real Estate For Best Home</p>
  <span class="social" style="left:865px;background:#4b6cb0" aria-label="Social profile"></span>
  <span class="social" style="left:931px;background:#2fa9e1" aria-label="Social profile"></span>
  <span class="social" style="left:997px;background:#454545" aria-label="Social profile"></span>
  <span class="social" style="left:1061px;background:#ee6b6b" aria-label="Social profile"></span>
</section>

<footer class="site-footer">
  <div class="foot-col" style="left:107px;width:215px">
    <h4>ABOUT BUSINESS</h4>
    <p>Lorem Ipsum dolor sit amet, consec-tetur adipisicing elit, sed do eiusmod tempor et incididunt ut labore et dolore</p>
  </div>
  <div class="foot-col" style="left:387px">
    <h4>OUR SERVICES</h4>
    <ul><li>Lorem Ipsum</li><li>Dolor sitmet, consectetur</li><li>Adipiscing elit</li><li>Vivamus porta, turpis</li><li>Aliquet semperaugue</li><li>Libero lobortis lacus</li></ul>
  </div>
  <div class="foot-col" style="left:644px">
    <h4>CONTACT US</h4>
    <p style="margin-bottom:10px">info@portalia.example</p>
    <p style="margin-bottom:10px">(012) 5550 1284</p>
    <p>4120 Velmora Road,<br>Glenhaven, California, USA</p>
  </div>
  <div class="foot-col" style="left:884px">
    <h4>NEWSLETTER</h4>
    <div class="news-field"><svg width="20" height="14" fill="none" stroke="#999" stroke-width="1.6"><rect x="1" y="1" width="18" height="12"/><path d="M1 1 L10 8 L19 1"/></svg>Email Adress</div>
    <div class="news-btn">SUBSCRIBE</div>
    <p style="margin-top:8px">400+ Subcribers</p>
  </div>
</footer>

<div class="copyright">Portalia © 2016 All Rights Reserved</div>

</body>
</html>
```